Pitch Deck Design for Startup (Zovo.io)

Graphic Design for Pitch Deck [Pitch Deck content in links below]

Who are we ?

“Zovo” always, never “ZOVO”

Zovo is an platform to easily use & publish algorithms with minimal effort.

Algorithms include:
Artificial Intelligence
Deep Learning
Machine Learning

No matter what type of applications or software users have, they can implement any of our State-of-Art AI algorithms in their apps with 3 lines of code.

Zovo is taming the tangle™

Using Zovo is as easy as just 3 lines of code to be up and running in minutes.

The general idea is that there's a central place for any app to find great algorithms when they want to use AI algorithms/models and implement them with extreme ease and speed, and this place is Zovo.io.

For the information this deck needs to contain, please refer to this google slide: http://lnkq.example/7Rt2kPw, all the information in there are necessary, we need you to transform this deck into a much better looking, clear, colorful, and also stylish & concise deck. If you can give it a bit of Sci-Fi style would be great as well (not a must have)!

You have total freedom to design however you want, just remember three principles:

It needs to establish the brand / image of the Zovo platform to the description above.

Our audience is wide - so use the ‘explain it like I am 5 year-old’ principle.

DO NOT assume specialist knowledge in the audience - make the deck extremely simple, clear, intuitive and compelling!
If there’s something you’re not sure about in the deck, anything, please don’t hesitate to ask us to get it right!!!

In terms of styles, what we like is something fun & modern but doesn’t lose a sense of quality (seriousness).

We want a clear storyline, and the current sequence and the way we organise the info is what we think is good, but it might not be the best way to present in the deck… additional slide ideas can be submitted with in the process.

QUESTIONS? If you have any questions or better suggestions on ANYTHING related to the deck, feel free to let us know at a@zovo.io, we normally respond promptly.

The design of our website uses more than one colors, and it has slight movement when people scrolling as well. Something goes along with its design would be a nice attribute (Note: not a must have, feel free to design your way, if you try to go along with those colors but the deck doesn’t look good, the design would have a very low chance of being selected). Please take a look for your inspirations: http://zovo.io.

Again, any questions, and enquiries, feel free to reach out to us: a@zovo.io

Target Market(s)

Angel Investors (Tech Startups), Developers, Software Companies

Industry/Entity Type

Startup

Font styles to use
Serif

Requirements
Must have
• GOOD DECKS EXAMPLES:
• For your reference, here are some deck designs we like:
• Vantro, NestLoop, Palvermo
• http://lnkq.example/4Hq9ZmD. The reason is: they are simple, clean, right on target, they used very simple but very friendly & nice colors. On every slide, the audience can kinda get the idea at the very first glance.
Nice to have
• If you can use multiple colors (themed in our style) , that would be awesome!
Should not have
• BAD DECKS EXAMPLES:
• The ones we don’t like: http://lnkq.example/8Wn3tbF, http://lnkq.example/5Jc6XrE. The reason? These are very tedious, not intuitive, and the design is very old fashioned. The information design of the deck is not giving great intuitions at the first sight, the audience has to go through all the text to get the idea.

```html
<!DOCTYPE html>
<html lang="en">
<head>
<meta charset="utf-8">
<title>Zovo Pitch Deck</title>
<link href="https://fonts.googleapis.com/css2?family=Oswald:wght@400;500&family=Montserrat:wght@400;500;600;700&display=swap" rel="stylesheet">
<style>
:root{
  --stage-light:#f1f1f2;
  --stage-dark:#333333;
  --ink:#1d1d24;
  --muted:#6b6b78;
  --violet:#7b74e6;
  --violet-band:#6f78de;
  --violet-soft:#b8a6ec;
  --lilac:#c79be0;
  --sky:#4cc3f4;
  --white:#ffffff;
  --photo-a:#e9edf6;
  --photo-b:#b8c3da;
  --photo-c:#4a5f8f;
}
*{box-sizing:border-box;margin:0;padding:0}
html,body{width:912px;height:1200px;overflow:hidden}
body{font-family:"Montserrat",sans-serif;color:var(--ink);background:var(--stage-dark);position:relative}
.stage-top{position:absolute;left:0;top:0;width:912px;height:612px;background:var(--stage-light)}
.stage-bottom{position:absolute;left:0;top:612px;width:912px;height:588px;background:var(--stage-dark)}
.hero{position:absolute;left:156px;top:137px;width:599px;height:337px;box-shadow:0 14px 30px rgba(0,0,0,.18)}
.hero .slide{transform:scale(1.44);transform-origin:0 0;position:absolute;left:0;top:0;box-shadow:none}
.slide{position:absolute;width:416px;height:234px;background:var(--white);overflow:hidden;box-shadow:0 6px 18px rgba(0,0,0,.35)}
.slide-1{left:35px;top:656px}
.slide-2{left:468px;top:656px}
.slide-3{left:35px;top:916px}
.slide-4{left:468px;top:916px}
.cover-photo{position:absolute;inset:0;background:linear-gradient(135deg,var(--photo-c) 0%,var(--photo-b) 30%,var(--photo-a) 60%,var(--photo-b) 85%,var(--photo-c) 100%)}
.cover-badge{position:absolute;inset:0}
.slide-tab{position:absolute;top:0;height:4px;background:var(--violet-soft)}
.slide-title{position:absolute;left:26px;top:14px;font-family:"Oswald",sans-serif;font-weight:400;font-size:18px;letter-spacing:.2px;color:var(--ink)}
.brand{position:absolute;right:16px;top:12px;display:flex;align-items:center;gap:3px;font-weight:700;font-size:9px;color:var(--violet)}
.brand-dot{width:8px;height:8px;border-radius:50%;background:var(--violet)}
.slide--violet{background:var(--violet-band)}
.slide--violet .slide-title,.slide--violet .brand{color:var(--white)}
.slide--violet .brand-dot{background:var(--white)}
.slide--violet .slide-tab{background:#e5e2fb}
.slide-footer{position:absolute;left:0;right:0;bottom:0;height:15px;background:var(--violet-band);display:flex;align-items:center;justify-content:center;gap:8px}
.slide--violet .slide-footer{background:#6670d6}
.footer-rule{width:66px;height:1px;background:rgba(255,255,255,.6);position:relative}
.footer-rule::before{content:"";position:absolute;top:-1.5px;width:4px;height:4px;border-radius:50%;border:1px solid rgba(255,255,255,.8)}
.footer-rule--left::before{left:0}
.footer-rule--right::before{right:0}
.footer-url{font-size:4.5px;letter-spacing:2px;color:var(--white)}
.page-no{position:absolute;right:16px;font-size:4.5px;color:var(--white)}
.chart{position:absolute;left:20px;top:58px;width:380px;height:140px}
.chart-source{position:absolute;left:0;right:0;top:205px;text-align:center;font-size:5px;font-weight:600;letter-spacing:.3px}
.challenge-arc{position:absolute;left:0;top:0;width:416px;height:234px}
.challenge-brand{position:absolute;left:42px;top:110px;display:flex;align-items:center;gap:6px;font-weight:600;font-size:19px;color:var(--ink)}
.challenge-brand .brand-dot{width:20px;height:20px;background:var(--violet)}
.challenge-list{position:absolute;left:205px;top:0;width:200px}
.challenge{position:absolute;left:0;width:200px}
.challenge h3,.trend h3{font-size:4.8px;font-weight:700;letter-spacing:.2px;margin-bottom:2px}
.challenge p,.trend p{font-size:4px;line-height:1.5;color:var(--muted);padding-left:7px;position:relative}
.challenge p::before,.trend p::before{content:"";position:absolute;left:0;top:1.2px;width:3.5px;height:3.5px;border-radius:50%;border:.6px solid var(--violet)}
.trend-map{position:absolute;left:20px;top:40px;width:300px;height:170px;background:radial-gradient(ellipse at center,rgba(255,255,255,.10),rgba(255,255,255,0) 70%)}
.trend-diagram{position:absolute;left:28px;top:58px;width:170px;height:150px;border-radius:50%;background:radial-gradient(circle at 50% 50%,rgba(255,255,255,.95) 0%,rgba(255,255,255,.75) 45%,rgba(255,255,255,0) 72%)}
.trend-list{position:absolute;left:236px;top:68px;width:160px;border-left:.8px solid rgba(255,255,255,.6);padding-left:8px}
.trend{position:relative;margin-bottom:9px;color:var(--white)}
.trend::before{content:"";position:absolute;left:-10.6px;top:0;width:4px;height:4px;border-radius:50%;background:var(--white)}
.trend p{color:rgba(255,255,255,.85)}
.trend p::before{border-color:var(--white)}
</style>
</head>
<body>

<div class="stage-top"></div>
<div class="stage-bottom"></div>

<div class="hero">
  <section class="slide slide--cover">
    <div class="cover-photo" role="img" aria-label="Photo of business people reviewing printed documents with a pen"></div>
    <svg class="cover-badge" viewBox="0 0 416 234" aria-hidden="true">
      <polygon points="208,34 100,196 316,196" fill="#ffffff" fill-opacity=".9"/>
      <polygon points="208,44 112,190 304,190" fill="none" stroke="#8a80e6" stroke-width=".8"/>
      <line x1="128" y1="164" x2="288" y2="164" stroke="#8a80e6" stroke-width=".8"/>
      <circle cx="208" cy="100" r="13" fill="#7b74e6"/>
      <text x="208" y="145" text-anchor="middle" font-family="Montserrat, sans-serif" font-weight="600" font-size="26" fill="#1d1d24">Zovo</text>
      <text x="208" y="181" text-anchor="middle" font-family="Montserrat, sans-serif" font-weight="500" font-size="8" fill="#1d1d24">AI ANYWHERE, ANYTIME</text>
    </svg>
  </section>
</div>

<section class="slide slide--cover slide-1">
  <div class="cover-photo" role="img" aria-label="Photo of business people reviewing printed documents with a pen"></div>
  <svg class="cover-badge" viewBox="0 0 416 234" aria-hidden="true">
    <polygon points="208,34 100,196 316,196" fill="#ffffff" fill-opacity=".9"/>
    <polygon points="208,44 112,190 304,190" fill="none" stroke="#8a80e6" stroke-width=".8"/>
    <line x1="128" y1="164" x2="288" y2="164" stroke="#8a80e6" stroke-width=".8"/>
    <circle cx="208" cy="100" r="13" fill="#7b74e6"/>
    <text x="208" y="145" text-anchor="middle" font-family="Montserrat, sans-serif" font-weight="600" font-size="26" fill="#1d1d24">Zovo</text>
    <text x="208" y="181" text-anchor="middle" font-family="Montserrat, sans-serif" font-weight="500" font-size="8" fill="#1d1d24">AI ANYWHERE, ANYTIME</text>
  </svg>
</section>

<section class="slide slide-2">
  <div class="slide-tab" style="left:22px;width:176px"></div>
  <h2 class="slide-title">EVERYONE WANTS AI</h2>
  <div class="brand"><span class="brand-dot"></span>Zovo</div>
  <svg class="chart" viewBox="0 0 380 140" aria-label="Area chart of rising interest in AI">
    <defs>
      <linearGradient id="chartFill" x1="0" y1="0" x2="1" y2="0">
        <stop offset="0" stop-color="#4cc3f4"/>
        <stop offset=".5" stop-color="#8e8ae8"/>
        <stop offset="1" stop-color="#d4a6e2"/>
      </linearGradient>
      <marker id="pt" viewBox="0 0 4 4" refX="2" refY="2" markerWidth="2.4" markerHeight="2.4"><circle cx="2" cy="2" r="1.6" fill="#2a2a33"/></marker>
    </defs>
    <path fill="url(#chartFill)" d="M0,140 L0,112 9.7,108 19.5,114 29.2,110 39,116 48.7,112 58.5,109 68.2,115 78,111 87.7,113 97.4,117 107.2,112 116.9,114 126.7,110 136.4,116 146.2,120 155.9,113 165.6,118 175.4,112 185.1,110 194.9,114 204.6,108 214.4,110 224.1,104 233.8,106 243.6,100 253.3,104 263.1,96 272.8,92 282.6,80 292.3,88 302.1,74 311.8,84 321.5,60 331.3,48 341,30 350.8,12 360.5,20 370.3,8 380,16 L380,140 Z"/>
    <polyline fill="none" stroke="#2a2a33" stroke-width=".5" stroke-opacity=".4" marker-start="url(#pt)" marker-mid="url(#pt)" marker-end="url(#pt)" points="0,112 9.7,108 19.5,114 29.2,110 39,116 48.7,112 58.5,109 68.2,115 78,111 87.7,113 97.4,117 107.2,112 116.9,114 126.7,110 136.4,116 146.2,120 155.9,113 165.6,118 175.4,112 185.1,110 194.9,114 204.6,108 214.4,110 224.1,104 233.8,106 243.6,100 253.3,104 263.1,96 272.8,92 282.6,80 292.3,88 302.1,74 311.8,84 321.5,60 331.3,48 341,30 350.8,12 360.5,20 370.3,8 380,16"/>
  </svg>
  <p class="chart-source">SOURCE _ QUERYLENS TRENDS</p>
  <footer class="slide-footer"><span class="footer-rule footer-rule--left"></span><span class="footer-url">www.zovo.io</span><span class="footer-rule footer-rule--right"></span><span class="page-no">01</span></footer>
</section>

<section class="slide slide-3">
  <div class="slide-tab" style="left:0;width:66px"></div>
  <h2 class="slide-title">BUT</h2>
  <div class="brand"><span class="brand-dot"></span>Zovo</div>
  <svg class="challenge-arc" viewBox="0 0 416 234" aria-hidden="true">
    <defs>
      <linearGradient id="iconFill" x1="0" y1="0" x2="1" y2="1">
        <stop offset="0" stop-color="#4cc3f4"/><stop offset="1" stop-color="#9a7fe4"/>
      </linearGradient>
    </defs>
    <path d="M57,55 A72,72 0 0 1 57,185" transform="translate(32,0)" fill="none" stroke="#d0d0d6" stroke-width="1"/>
    <circle cx="57" cy="57" r="1.5" fill="#b9b9c2"/>
    <circle cx="57" cy="183" r="1.5" fill="#b9b9c2"/>
    <g fill="#fff" stroke-width="1">
      <circle cx="126" cy="58" r="2.6" stroke="#7b74e6"/>
      <circle cx="158" cy="98" r="2.6" stroke="#9a7fe4"/>
      <circle cx="158" cy="142" r="2.6" stroke="#b58be0"/>
      <circle cx="122" cy="184" r="2.6" stroke="#4cc3f4"/>
    </g>
    <g stroke="#b9b9c2" stroke-width=".6" stroke-dasharray="1.2 1.2">
      <line x1="129" y1="58" x2="186" y2="58"/>
      <line x1="161" y1="98" x2="186" y2="98"/>
      <line x1="161" y1="142" x2="186" y2="142"/>
      <line x1="125" y1="184" x2="186" y2="184"/>
    </g>
    <g fill="url(#iconFill)">
      <circle cx="193" cy="58" r="8"/><circle cx="193" cy="98" r="8"/>
      <circle cx="193" cy="142" r="8"/><circle cx="193" cy="184" r="8"/>
    </g>
    <g fill="none" stroke="#fff" stroke-width="1">
      <circle cx="193" cy="56" r="2"/><path d="M189,62 Q193,58 197,62"/>
      <circle cx="193" cy="98" r="3"/><circle cx="193" cy="98" r="1"/>
      <rect x="189" y="139" width="8" height="6" rx="1"/>
      <path d="M189,187 L192,183 194,185 197,180"/>
    </g>
  </svg>
  <div class="challenge-brand"><span class="brand-dot"></span>Zovo</div>
  <div class="challenge-list">
    <div class="challenge" style="top:53px"><h3>RARE TALENTS</h3><p>Well trained AI talents are really hard to find.</p></div>
    <div class="challenge" style="top:93px"><h3>LONG DEV PROCESS</h3><p>Finding the right AI solution &amp; AI development are time consuming.</p><p>Infrastructures need to be very well configured for the best performance.</p></div>
    <div class="challenge" style="top:137px"><h3>STEEP LEARNING CURVE</h3><p>AI takes a long time to learn, it's hard for normal developers to develop AI.</p><p>Even slightly customizing &amp; modifying AI algorithms can be challenging.</p></div>
    <div class="challenge" style="top:179px"><h3>REPEATED WORKS</h3><p>Most people are re-training the same/very similar AI models and hosting them separately for use.</p></div>
  </div>
  <footer class="slide-footer"><span class="footer-rule footer-rule--left"></span><span class="footer-url">www.zovo.io</span><span class="footer-rule footer-rule--right"></span><span class="page-no">02</span></footer>
</section>

<section class="slide slide--violet slide-4">
  <div class="slide-tab" style="left:22px;width:100px"></div>
  <h2 class="slide-title">MEANWHILE</h2>
  <div class="brand"><span class="brand-dot"></span>Zovo</div>
  <div class="trend-map" role="img" aria-label="Faint dotted world map in the background"></div>
  <div class="trend-diagram" role="img" aria-label="Circular infographic linking AI algorithmic interests, API boom and biggest tech trends"></div>
  <div class="trend-list">
    <div class="trend"><h3>AI ALGORITHMIC INTERESTS</h3><p>AI has been proven to deliver great results.</p><p>Digital products are (looking for) implementing AI in software.</p><p>AI has already become the "Next Big Thing".</p></div>
    <div class="trend"><h3>API BOOM</h3><p>Most sophisticated digital products are heavily relying on APIs to interconnect components &amp; integrate w/ services.</p><p>APIs are turning the world into a giant computer.</p></div>
    <div class="trend"><h3>ARE BIGGEST TECH TRENDS</h3></div>
  </div>
  <footer class="slide-footer"><span class="footer-rule footer-rule--left"></span><span class="footer-url">www.zovo.io</span><span class="footer-rule footer-rule--right"></span><span class="page-no">03</span></footer>
</section>

</body>
</html>
```